Flyer

I am a qualified accountant and I need a flyer to promote my business when networking

My services include
Management Accounts, Financial Accounts, Day to Day Bookkeeping services, business start up assistance
I will produce and submit Self Assessment Tax Returns, Annual Accounts, VAT tax returns, Payroll and PAYE

I attach my business card design so that there is some continuity if you think it appropiate.

Size A3 is preferred, please.

Sorry, I mean't Size A5 is preferred.

A5 please

Free initial consultations and advice.

```html
<!DOCTYPE html>
<html lang="en">
<head>
<meta charset="utf-8">
<title>Clara Moss Accounting – Flyer</title>
<link rel="stylesheet" href="https://fonts.googleapis.com/css2?family=Montserrat:wght@300;400;600;700;800&display=swap">
<style>
  :root {
    --green: #a8cf38;
    --green-text: #9fca2e;
    --band: #bfd93a;
    --band-edge: #a9cc34;
    --brand-dark: #3f7a2a;
    --white: #ffffff;
    --panel-top: #ffffff;
    --panel-bottom: #ebebeb;
  }
  * { margin: 0; padding: 0; box-sizing: border-box; }
  html, body { width: 933px; height: 1200px; overflow: hidden; background: var(--white); }
  body { font-family: "Montserrat", Arial, sans-serif; }
  .flyer { position: relative; width: 933px; height: 1200px; overflow: hidden; background: var(--white); }
  .text-panel {
    position: absolute; left: 0; top: 0; width: 509px; height: 1011px;
    background: linear-gradient(180deg, var(--panel-top) 0%, var(--panel-bottom) 100%);
  }
  .photo {
    position: absolute; left: 509px; top: 0; width: 368px; height: 1011px;
    background: linear-gradient(160deg, #eef2f6 0%, #cfd9e4 28%, #8b949e 52%, #4a4f57 68%, #6f7b88 82%, #b9cbe0 100%);
  }
  .t { position: absolute; left: 46px; color: var(--green-text); line-height: 1; white-space: nowrap; }
  .headline { font-size: 88px; letter-spacing: -3px; color: var(--green); }
  .headline.light { font-weight: 300; top: 40px; }
  .headline.bold { font-weight: 800; }
  .headline.you { top: 116px; }
  .headline.ahead { top: 192px; }
  .rule { position: absolute; left: 46px; width: 430px; height: 3px; background: var(--green); }
  .rule.top { top: 294px; }
  .rule.bottom { top: 853px; }
  .name { top: 333px; font-size: 57px; font-weight: 800; letter-spacing: -2px; color: var(--green); }
  .credentials { top: 388px; font-size: 36px; font-weight: 300; letter-spacing: -1px; color: var(--green); }
  .section-label { font-size: 21px; font-weight: 300; letter-spacing: -0.5px; }
  .label-services { top: 457px; }
  .label-submit { top: 641px; }
  .service-list { position: absolute; left: 46px; list-style: none; color: var(--green-text); font-size: 21.5px; font-weight: 700; letter-spacing: -0.6px; line-height: 26.4px; }
  .list-services { top: 508px; }
  .list-submit { top: 692px; }
  .call-to-action { top: 889px; font-size: 35px; font-weight: 800; letter-spacing: -1.5px; line-height: 34px; color: var(--green); }
  .contact-band { position: absolute; left: 0; top: 1011px; width: 933px; height: 189px; background: var(--band); border-top: 13px solid var(--band-edge); }
  .brand-name { position: absolute; left: 42px; top: 96px; width: 300px; text-align: center; font-size: 17px; font-weight: 600; letter-spacing: 0.5px; color: var(--brand-dark); }
  .icon { position: absolute; left: 366px; width: 68px; height: 68px; }
  .icon.phone { top: 29px; }
  .icon.email { top: 103px; }
  .phone-number { position: absolute; right: 58px; top: 38px; font-size: 53px; font-weight: 700; letter-spacing: -1.5px; color: var(--white); line-height: 1; }
  .email-address { position: absolute; right: 58px; top: 107px; text-align: right; font-size: 25px; font-weight: 700; letter-spacing: -0.5px; line-height: 25px; color: var(--white); }
</style>
</head>
<body>
<main class="flyer">
  <section class="text-panel">
    <h1>
      <span class="t headline light">KEEPING</span>
      <span class="t headline bold you">YOU</span>
      <span class="t headline bold ahead">AHEAD...</span>
    </h1>
    <div class="rule top"></div>
    <h2 class="t name">CLARA MOSS</h2>
    <p class="t credentials">ACMA / CGMA</p>
    <p class="t section-label label-services">MY SERVICES INCLUDE –</p>
    <ul class="service-list list-services">
      <li>MANAGEMENT ACCOUNTS</li>
      <li>FINANCIAL ACCOUNTS</li>
      <li>DAY TO DAY BOOKEEPING SERVICES</li>
      <li>BUSINESS START-UP ASSISTANCE</li>
    </ul>
    <p class="t section-label label-submit">I WILL PRODUCE &amp; SUBMIT –</p>
    <ul class="service-list list-submit">
      <li>SELF ASSESSMENT TAX RETURNS</li>
      <li>ANNUAL RETURNS</li>
      <li>VAT TAX RETURNS</li>
      <li>PAYROLL</li>
      <li>PAYE</li>
    </ul>
    <div class="rule bottom"></div>
    <p class="t call-to-action">CONTACT ME FOR<br>MORE INFORMATION...</p>
  </section>

  <div class="photo" role="img" aria-label="Photo of a finger pressing a calculator key over printed columns of figures"></div>

  <footer class="contact-band">
    <p class="brand-name">CLARA MOSS ACCOUNTING</p>
    <svg class="icon phone" viewBox="0 0 68 68" aria-hidden="true">
      <circle cx="34" cy="34" r="29" fill="none" stroke="#fff" stroke-width="5"/>
      <path d="M24 18c2-1 4-1 5 1l4 7c1 2 0 3-1 4l-3 2c2 5 6 9 11 11l2-3c1-1 3-2 4-1l7 4c2 1 2 3 1 5l-3 4c-2 2-5 2-8 1-11-4-19-12-23-23-1-3-1-6 1-8z" fill="#fff"/>
    </svg>
    <p class="phone-number">07700 900418</p>
    <svg class="icon email" viewBox="0 0 68 68" aria-hidden="true">
      <circle cx="34" cy="34" r="14" fill="none" stroke="#fff" stroke-width="5"/>
      <path d="M48 22v18c0 5 8 5 8-3v-3c0-12-10-22-22-22S12 22 12 34s10 22 22 22c5 0 9-1 12-3" fill="none" stroke="#fff" stroke-width="5" stroke-linecap="round"/>
    </svg>
    <p class="email-address">clara@<br>claramossaccounting.com</p>
  </footer>
</main>
</body>
</html>
```